Brighten Every Calling book cover and updated company logo bundle

USE THE LOGO ON THE BACK COVER. I WANT AN UPDATED LOOK TO MY LOGO
Size of book: 5.5 x 8.5
Title: Brighten Every Calling
Subtitle: An introvert’s guide to creating a coaching business that reflects who you are
The Subtitle does NOT go on the book cover
Author: Marla Toppington
BOOK DESCRIPTION: This book will help coaches and creative professionals get confidently clear on who they are so they can create a business that reflects their inner message.

DEMOGRAPHICS — Coaches and creative professional age 35-45

WOULD YOU PREFER PEOPLE OR OBJECTS ON YOUR COVER?
Objects or abstract designs
Anything I don’t want on the cover? people
Objects or symbols I want on the cover: possibly magnifying glass

IF YOU HAVE ANY PHOTOS THAT YOU WOULD LIKE US TO USE, PLEASE INCLUDE THE LINK(S) HERE. My logo or face pic for the back cover (Face pic pending)

COPY FOR THE SPINE
Brighten Every Calling
Marla Toppington
Lanternhall Books (with logo)

COPY FOR THE BACK COVER (270 words) my biz logo at the bottom and my picture next to my short bio. (Picture to come)

Create a Coaching Business that Reflects Who You Are

Do you want to step confidently into your new career by doing what you love? You aren't alone! But instead of doing what they love, many new coaches get stuck by trying to fit into traditional ways of doing business and create many unnecessary hurdles to happiness and success.
In this book, creative business coach, Marla Toppington teaches you, as she has taught herself and many others, to stop feeling guilty about what you “should” do in your life and in the process you will learn how to turn your passion into a purposeful career.

New coaches will learn how to:
• Recognize how your life decisions to this point are holding you back.
• Discover your gifts so you can express yourself through your creative projects.
• Identify and develop tools to bring your passion into purpose
• Offer services based on what you love to do.
• Understand your personal work style and work-flow to optimize your ideas and productivity.
• Create a message that reflects who you are to attract clients to work with you.
• Ask confidently for what you are worth and get it every time.
Join Marla on the journey of reconnecting with yourself and manifesting your dream.

Marla Toppington, founder of Quiet Harbor Wellness, helps new coaches and creative entrepreneurs find their inner voice so that they have the confidence to bring their authentic selves out into the world. Marla has gone through this process for herself and helped other new businesses achieve dramatic improvements in their organization and focus as a result.

Target Market(s)

indicated in description

Industry/Entity Type

Life Coaching

Logo Text

Quiet Harbor Wellness

Requirements
Must have
• updated look on existing logo it is going on the back of the book
Nice to have
• I like the font in the book cover I attached but Id like to see what else is possible

```html
<!DOCTYPE html>
<html lang="en">
<head>
<meta charset="utf-8">
<title>Brighten Every Calling — Cover Spread</title>
<link href="https://fonts.googleapis.com/css2?family=Anton&family=Andika:wght@400;700&family=Ubuntu:wght@400;500&display=swap" rel="stylesheet">
<style>
  :root {
    --page-bg: #ffffff;
    --cover-light: #ffffff;
    --cover-edge: #e4e5e6;
    --ink-blue: #2f4895;
    --ink-grey: #555555;
    --ink-dark: #333333;
    --placeholder: #ebebeb;
    --logo-orange: #c9521f;
  }
  * { margin: 0; padding: 0; box-sizing: border-box; }
  html, body {
    width: 1200px; height: 1000px; overflow: hidden;
    background: var(--page-bg);
  }
  .canvas { position: relative; width: 1200px; height: 1000px; }

  .cover-spread {
    position: absolute; left: 88px; top: 90px; width: 1034px; height: 772px;
    background: radial-gradient(ellipse at 55% 45%, var(--cover-light) 40%, var(--cover-edge) 100%);
    box-shadow: 0 1px 6px rgba(0,0,0,0.35);
    overflow: hidden;
  }

  /* Back cover */
  .back-cover { position: absolute; left: 0; top: 0; width: 477px; height: 100%; }
  .back-kicker {
    position: absolute; left: 0; width: 504px; top: 36px; text-align: center;
    font-family: "Ubuntu", sans-serif; font-size: 19px; line-height: 22px; color: var(--ink-dark);
  }
  .back-headline {
    position: absolute; left: 0; width: 504px; top: 56px; text-align: center;
    font-family: "Anton", sans-serif; font-size: 30px; letter-spacing: 1px;
    color: var(--ink-blue); line-height: 36px; font-weight: 400;
  }
  .back-blurb {
    position: absolute; left: 50px; top: 96px; width: 420px;
    font-family: "Andika", sans-serif; font-size: 14px; line-height: 17.6px;
    text-align: justify; color: var(--ink-dark);
  }
  .learn-heading {
    position: absolute; left: 54px; top: 268px;
    font-family: "Anton", sans-serif; font-size: 27px; letter-spacing: 0.6px;
    color: var(--ink-blue); line-height: 32px; font-weight: 400; white-space: nowrap;
  }
  .learn-list {
    position: absolute; left: 48px; top: 305px; width: 440px;
    list-style: none;
    font-family: "Andika", sans-serif; font-size: 9.2px; line-height: 11px; color: var(--ink-dark);
  }
  .learn-list li { position: relative; padding-left: 12px; height: 17.3px; white-space: nowrap; }
  .learn-list li::before {
    content: ""; position: absolute; left: 0; top: 3.5px;
    width: 4px; height: 4px; border-radius: 50%; background: var(--ink-blue);
  }
  .author-photo {
    position: absolute; left: 50px; top: 492px; width: 87px; height: 115px;
    background: var(--placeholder);
  }
  .bio-name {
    position: absolute; left: 144px; top: 484px;
    font-family: "Ubuntu", sans-serif; font-size: 18px; line-height: 20px; letter-spacing: 3.6px;
    color: var(--ink-grey); white-space: nowrap;
  }
  .bio-text {
    position: absolute; left: 144px; top: 507px; width: 317px;
    font-family: "Andika", sans-serif; font-size: 12.8px; line-height: 15.3px;
    text-align: justify; color: var(--ink-blue);
  }
  .brand-mark {
    position: absolute; left: 62px; top: 668px;
    display: flex; align-items: center; gap: 8px; white-space: nowrap;
    font-family: "Andika", sans-serif; font-size: 17px; line-height: 22px; color: var(--logo-orange);
  }
  .brand-mark .dot { width: 18px; height: 18px; border-radius: 50%; background: var(--logo-orange); flex: none; }
  .isbn-box {
    position: absolute; left: 298px; top: 633px; width: 176px; height: 105px;
    background: #ffffff; border: 1px solid #e6e6e6;
  }

  /* Spine */
  .spine { position: absolute; left: 477px; top: 0; width: 60px; height: 100%; }
  .spine-title, .spine-author {
    position: absolute; left: 50%; white-space: nowrap;
    transform-origin: 0 0;
  }
  .spine-title {
    top: 38px; transform: translateX(22px) rotate(90deg);
    font-family: "Anton", sans-serif; font-size: 35px; line-height: 44px;
    color: var(--ink-blue);
  }
  .spine-title .grey { color: var(--ink-grey); }
  .spine-author {
    top: 478px; transform: translateX(12px) rotate(90deg);
    font-family: "Ubuntu", sans-serif; font-size: 18px; letter-spacing: 5.5px;
    line-height: 24px; color: var(--ink-grey);
  }

  /* Front cover */
  .front-cover { position: absolute; left: 537px; top: 0; width: 497px; height: 100%; }
  .front-title {
    position: absolute; left: 0; width: 497px; top: 46px; text-align: center;
    font-family: "Anton", sans-serif; font-weight: 400;
    color: var(--ink-blue); letter-spacing: 2px;
  }
  .front-title span { display: block; font-size: 112px; line-height: 100px; height: 100px; white-space: nowrap; }
  .front-title .grey { color: var(--ink-grey); font-size: 104px; height: 118px; }
  .magnifier-art {
    position: absolute; left: 80px; top: 395px; width: 390px; height: 310px;
  }
  .front-author {
    position: absolute; left: 0; width: 497px; top: 714px; text-align: center;
    font-family: "Ubuntu", sans-serif; font-size: 18px; letter-spacing: 5px;
    color: var(--ink-dark);
  }
</style>
</head>
<body>
<div class="canvas">
  <div class="cover-spread">

    <section class="back-cover">
      <p class="back-kicker">Create a Coaching Business that</p>
      <h2 class="back-headline">REFLECTS WHO YOU ARE</h2>
      <p class="back-blurb">Do you want to step confidently into your new career by doing what you love? You aren't alone! But instead of doing what they love, many new coaches get stuck by trying to fit into traditional ways of doing business and create many unnecessary hurdles to happiness and success.<br>In this book, creative business coach, Marla Toppington teaches you, as she has taught herself and many others, to stop feeling guilty about what you “should” do in your life and in the process you will learn how to turn your passion into a purposeful career.</p>

      <h3 class="learn-heading">NEW COACHES WILL LEARN HOW TO:</h3>
      <ul class="learn-list">
        <li>Recognize how your life decisions to this point are holding you back.</li>
        <li>Discover your gifts so you can express yourself through your creative projects.</li>
        <li>Identify and develop tools to bring your passion into purpose</li>
        <li>Offer services based on what you love to do.</li>
        <li>Understand your personal work style and work-flow to optimize your ideas and productivity.</li>
        <li>Create a message that reflects who you are to attract clients to work with you.</li>
        <li>Ask confidently for what you are worth and get it every time.</li>
        <li>Join Marla on the journey of reconnecting with yourself and manifesting your dream.</li>
      </ul>

      <div class="author-photo" role="img" aria-label="Author portrait placeholder"></div>
      <p class="bio-name">MARLA TOPPINGTON</p>
      <p class="bio-text">founder of Quiet Harbor Wellness, helps new coaches and creative entrepreneurs find their inner voice so that they have the confidence to bring their authentic selves out into the world. Marla has gone through this process for herself and helped other new businesses achieve dramatic improvements in their organization and focus as a result.</p>

      <div class="brand-mark"><span class="dot"></span><span>Quiet Harbor Wellness</span></div>
      <div class="isbn-box"></div>
    </section>

    <section class="spine">
      <p class="spine-title"><span class="grey">BRIGHTEN</span> EVERY CALLING</p>
      <p class="spine-author">MARLA TOPPINGTON</p>
    </section>

    <section class="front-cover">
      <h1 class="front-title">
        <span class="grey">BRIGHTEN</span>
        <span>EVERY</span>
        <span>CALLING</span>
      </h1>
      <svg class="magnifier-art" viewBox="0 0 390 310" role="img" aria-label="Illustration of a silver magnifying glass with a blue lens casting a soft shadow">
        <defs>
          <radialGradient id="lensTone" cx="45%" cy="40%" r="60%">
            <stop offset="0%" stop-color="#7fa4d8"/>
            <stop offset="60%" stop-color="#b8c9e2"/>
            <stop offset="100%" stop-color="#dcdfe3" stop-opacity="0"/>
          </radialGradient>
        </defs>
        <rect width="390" height="310" fill="url(#lensTone)"/>
      </svg>
      <p class="front-author">MARLA TOPPINGTON</p>
    </section>

  </div>
</div>
</body>
</html>
```